Re-design of Business Card

We require a design for our business card.

Korrim is a supplier of industrial packaging specializing in plastic products. We are undergoing a rebranding to appear more corporate. We have changed our company name to korrim and have a new logo.

I have uploaded our old card design with the previous company name.
Don't copy the current design. We are looking for a new design.

Industry/Entity Type

Manufacturing

Contact Information for Business Card

please don't copy the current design. we are looking for a new design.

Font styles to use
Sans Serif

Colors

Designer to choose colors to be used in the design.

Requirements
Must have
• clean and easy to read.

```html
<!DOCTYPE html>
<html lang="en">
<head>
<meta charset="utf-8">
<title>Korrim Business Card</title>
<link href="https://fonts.googleapis.com/css2?family=Source+Sans+3:wght@400;600;700&display=swap" rel="stylesheet">
<style>
:root{
  --page:#3a3d40;
  --card:#252525;
  --orange:#f27f1f;
  --white:#f4f4f4;
  --text:#cfcfcf;
}
*{margin:0;padding:0;box-sizing:border-box}
html,body{width:1200px;height:720px;overflow:hidden;background:var(--page)}
body{position:relative;font-family:"Source Sans 3",sans-serif}
.card{position:absolute;top:222px;width:450px;height:277px;background:var(--card);box-shadow:4px 6px 12px rgba(0,0,0,.45);overflow:hidden}
.card--front{left:107px}
.card--back{left:622px}
.card__bands{position:absolute;inset:0}
.brand-name{position:absolute;left:47px;top:48px;width:152px;height:42px;display:flex;align-items:center;justify-content:center;color:var(--orange);font-weight:700;font-size:31px;letter-spacing:1px;line-height:1}
.region-map{position:absolute;left:15px;top:105px;width:120px;height:87px;border:1px solid var(--orange);background:linear-gradient(135deg,#2e2a27,#3a2c20)}
.cert-badge{position:absolute;top:103px;width:82px;height:80px;border:6px solid var(--orange);border-radius:50%;border-top-color:transparent}
.cert-badge--one{left:148px}
.cert-badge--two{left:248px}
.cert-badge--three{left:347px}
.services{position:absolute;left:15px;top:207px;font-size:8.7px;line-height:12.4px}
.services__row{display:flex}
.services__name{width:131px;color:var(--orange);font-weight:700;text-transform:uppercase}
.services__detail{color:var(--text)}
.person{position:absolute;left:53px;top:162px}
.person__name{color:var(--orange);font-size:13px;line-height:16px}
.person__title{color:var(--orange);font-size:10px;line-height:12px}
.contact-line{display:flex;align-items:center;gap:6px;font-size:10.5px;line-height:12.5px}
.person .contact-line{color:var(--orange)}
.person__contacts{margin-top:7px}
.divider{position:absolute;left:206px;top:148px;width:1px;height:71px;background:var(--orange)}
.company{position:absolute;left:231px;top:146px;color:var(--text)}
.company__address{font-size:11px;line-height:14px;margin-bottom:5px}
.company .contact-line{font-size:11px;line-height:14.5px}
.icon{width:10px;height:10px;flex:none}
</style>
</head>
<body>

<section class="card card--front">
  <svg class="card__bands" viewBox="0 0 450 277" width="450" height="277" aria-hidden="true">
    <rect x="0" y="43" width="450" height="52" fill="#f4f4f4"/>
    <rect x="0" y="48" width="450" height="42" fill="#f27f1f"/>
    <rect x="47" y="48" width="152" height="42" fill="#f4f4f4"/>
    <polygon points="366,48 375,48 403,90 394,90" fill="#f4f4f4"/>
    <rect x="0" y="270" width="450" height="7" fill="#f27f1f"/>
    <polygon points="263,270 270,270 275,277 268,277" fill="#252525"/>
  </svg>
  <div class="brand-name">KORRIM</div>
  <div class="region-map" role="img" aria-label="Outline map of Australia and New Zealand with distribution location pins"></div>
  <div class="cert-badge cert-badge--one"></div>
  <div class="cert-badge cert-badge--two"></div>
  <div class="cert-badge cert-badge--three"></div>
  <div class="services">
    <div class="services__row"><span class="services__name">Pallet Containment</span><span class="services__detail">Stretch, Heat Shrink, Pallet Hood</span></div>
    <div class="services__row"><span class="services__name">Flexible Packaging</span><span class="services__detail">Baos &amp; Liners, Tube, Film &amp; Sheet, Printed Films(12 col), Shrink films</span></div>
    <div class="services__row"><span class="services__name">Pallet Wrapping Machinery</span><span class="services__detail">Semi &amp; Fully Auto Lines, Finance Options Include Lease, Rent, Pay per wrap</span></div>
    <div class="services__row"><span class="services__name">General Packaging</span></div>
  </div>
</section>

<section class="card card--back">
  <svg class="card__bands" viewBox="0 0 450 277" width="450" height="277" aria-hidden="true">
    <rect x="0" y="43" width="450" height="52" fill="#f4f4f4"/>
    <rect x="0" y="48" width="450" height="42" fill="#f27f1f"/>
    <rect x="47" y="48" width="152" height="42" fill="#f4f4f4"/>
    <polygon points="366,48 375,48 403,90 394,90" fill="#f4f4f4"/>
    <rect x="0" y="270" width="450" height="7" fill="#f27f1f"/>
    <polygon points="263,270 270,270 275,277 268,277" fill="#252525"/>
  </svg>
  <div class="brand-name">KORRIM</div>

  <div class="person">
    <div class="person__name">Dorian Platt</div>
    <div class="person__title">Machinery Sales Manager</div>
    <div class="person__contacts">
      <div class="contact-line">
        <svg class="icon" viewBox="0 0 10 10"><path d="M2 1l2 0 1 2.3-1.2.9a6 6 0 0 0 2.2 2.2l.9-1.2L9 6v2c0 .6-.5 1-1 1C4.5 9 1 5.5 1 2c0-.5.4-1 1-1z" fill="#f27f1f"/></svg>
        <span>XXXX XXX XXX</span>
      </div>
      <div class="contact-line">
        <svg class="icon" viewBox="0 0 10 10"><rect x="0" y="2" width="10" height="7" fill="#f27f1f"/><path d="M0 2l5 4 5-4" stroke="#252525" stroke-width="1" fill="none"/></svg>
        <span>dorian@korrim.com.au</span>
      </div>
    </div>
  </div>

  <div class="divider"></div>

  <div class="company">
    <div class="company__address">48 Marlow St Eastbrook Park,<br>Qld 4170 Australia</div>
    <div class="contact-line">
      <svg class="icon" viewBox="0 0 10 10"><path d="M1 4c0-2 8-2 8 0v1H7V4H3v1H1z" fill="#f27f1f"/><rect x="2" y="5" width="6" height="4" rx="1" fill="#f27f1f"/></svg>
      <span>1300 555 418</span>
    </div>
    <div class="contact-line">
      <svg class="icon" viewBox="0 0 10 10"><rect x="3" y="0.5" width="4" height="3" fill="#f27f1f"/><rect x="1" y="4" width="8" height="3.5" rx="1" fill="#f27f1f"/><rect x="2.5" y="7.5" width="5" height="2" fill="#f27f1f"/></svg>
      <span>+61 7 3555 0192</span>
    </div>
    <div class="contact-line">
      <svg class="icon" viewBox="0 0 10 10"><circle cx="5" cy="5" r="4.3" fill="#f27f1f"/><path d="M0.7 5h8.6M5 .7c-2.4 2.6-2.4 6 0 8.6M5 .7c2.4 2.6 2.4 6 0 8.6" stroke="#252525" stroke-width=".7" fill="none"/></svg>
      <span>www.korrimpackaging.com.au</span>
    </div>
  </div>
</section>

</body>
</html>
```